Warehouse Clearance Sale Poster

We need a poster for an upcoming warehouse sale of badminton equipments which have up to 70% off and free mystery gift available when spend over $50.

Event will be on 5-7 Oct (10am-10pm) 3 DAYS ONLY
location: Unit 5 Marlowe Fenwick Lane, Tarrowby, 2087, NSW

Event will only happen every 2 years.

Products include Rackets,Tournament Bag, Apparels and Accessories.

The file attached is a sample we have found online that we liked. So feel free to base the design on that or design something completely new.

Target Market(s)

Current Badminton Player

Industry/Entity Type

Sporting Good

Colors
f37122
f78f20
f68e4e
0655a3
3277b5
3377b5

Requirements
Must have
• up to 70% off (Big Font)
• KESTAL logo (equipement brand)
• few players images
Nice to have
• Badminton Theme (with equipment)

```html
<!DOCTYPE html>
<html lang="en">
<head>
<meta charset="utf-8">
<title>Warehouse Sale Poster</title>
<link rel="stylesheet" href="https://fonts.googleapis.com/css2?family=Luckiest+Guy&family=Open+Sans:wght@600;700;800&display=swap">
<style>
  :root {
    --orange: #f37122;
    --orange-light: #f78f20;
    --orange-soft: #f68e4e;
    --blue-deep: #0655a3;
    --blue: #3277b5;
    --yellow: #f6c514;
    --gold: #f39a1c;
    --white: #ffffff;
    --silhouette: #333333;
  }
  * { margin: 0; padding: 0; box-sizing: border-box; }
  html, body { width: 880px; height: 1200px; overflow: hidden; background: var(--orange); }
  .poster {
    position: relative;
    width: 880px;
    height: 1200px;
    overflow: hidden;
    background: radial-gradient(circle at 50% 45%, var(--orange-light) 0%, var(--orange) 70%);
    font-family: "Open Sans", sans-serif;
  }
  .poster-shapes { position: absolute; inset: 0; }
  .inner-frame {
    position: absolute;
    left: 30px; top: 23px; width: 821px; height: 1153px;
    border: 3px solid var(--white);
  }
  .brand {
    position: absolute;
    right: 60px; top: 44px;
    display: flex; align-items: center; gap: 8px;
    color: var(--white);
    font-family: "Open Sans", sans-serif;
    font-size: 24px; font-weight: 800;
    letter-spacing: 1px;
  }
  .brand-dot { width: 14px; height: 14px; border-radius: 50%; background: var(--white); }
  .headline {
    position: absolute;
    left: 100px;
    font-family: "Luckiest Guy", sans-serif;
    font-weight: 400;
    line-height: 1;
    background: linear-gradient(180deg, #ffffff 0%, #f2f2f2 45%, #bdbdbd 55%, #ffffff 100%);
    -webkit-background-clip: text;
    background-clip: text;
    -webkit-text-fill-color: transparent;
    filter: drop-shadow(3px 4px 0 #3a3a3a);
  }
  .headline-warehouse { top: 80px; font-size: 84px; }
  .headline-sale { top: 178px; font-size: 96px; }
  .player-main {
    position: absolute;
    left: 628px; top: 230px; width: 210px; height: 480px;
    border-radius: 90px 90px 60px 60px;
    background: linear-gradient(180deg, #3a3a3a 0%, var(--silhouette) 100%);
  }
  .player-faint {
    position: absolute;
    border-radius: 40px;
    background: var(--orange-soft);
    opacity: 0.55;
  }
  .player-faint-top { left: 740px; top: 150px; width: 70px; height: 70px; }
  .player-faint-left { left: 50px; top: 560px; width: 60px; height: 130px; }
  .discount {
    position: absolute;
    font-family: "Luckiest Guy", sans-serif;
    line-height: 1;
    background: linear-gradient(180deg, var(--yellow) 0%, var(--gold) 100%);
    -webkit-background-clip: text;
    background-clip: text;
    -webkit-text-fill-color: transparent;
    filter: drop-shadow(3px 3px 0 var(--white)) drop-shadow(2px 3px 0 #0a3f7c);
    transform: rotate(-6deg);
  }
  .discount-upto { left: 188px; top: 430px; font-size: 84px; }
  .discount-number { left: 190px; top: 515px; font-size: 170px; }
  .discount-percent { left: 420px; top: 525px; font-size: 76px; }
  .discount-off { left: 425px; top: 595px; font-size: 66px; }
  .gift-note {
    position: absolute;
    left: 120px; width: 520px; top: 800px;
    text-align: center;
    color: var(--white);
    font-size: 20px; font-weight: 800;
  }
  .event-info {
    position: absolute;
    left: 110px; width: 640px;
    text-align: center;
    color: var(--white);
  }
  .event-dates { top: 883px; font-size: 36px; font-weight: 700; }
  .event-duration { top: 930px; font-size: 35px; font-weight: 700; letter-spacing: 0.5px; }
  .event-location { top: 980px; font-size: 15px; font-weight: 600; }
  .event-frequency { top: 1021px; left: 120px; width: 610px; font-size: 21px; font-weight: 800; }
  .product-list {
    position: absolute;
    left: 30px; width: 821px; top: 1118px;
    display: flex; justify-content: center; align-items: center;
    list-style: none;
    color: var(--white);
    font-size: 20px; font-weight: 700;
  }
  .product-list li + li::before {
    content: "";
    display: inline-block;
    width: 2px; height: 16px;
    background: var(--white);
    margin: 0 12px;
    vertical-align: -1px;
  }
</style>
</head>
<body>
<div class="poster">
  <svg class="poster-shapes" width="880" height="1200" viewBox="0 0 880 1200">
    <defs>
      <radialGradient id="badge-burst" cx="55%" cy="50%" r="60%">
        <stop offset="0%" stop-color="#2f8ae8"/>
        <stop offset="100%" stop-color="#0a57b8"/>
      </radialGradient>
      <linearGradient id="info-band" x1="0" y1="0" x2="1" y2="0">
        <stop offset="0%" stop-color="#0655a3"/>
        <stop offset="60%" stop-color="#1a73d9"/>
        <stop offset="100%" stop-color="#2a8cf0"/>
      </linearGradient>
      <linearGradient id="gold-band" x1="0" y1="0" x2="1" y2="0">
        <stop offset="0%" stop-color="#f39a1c"/>
        <stop offset="100%" stop-color="#f6c514"/>
      </linearGradient>
    </defs>

    <g class="ambient-dots" fill="#f68e4e" opacity="0.55">
      <circle cx="790" cy="820" r="40"/>
      <circle cx="810" cy="1100" r="30"/>
      <circle cx="115" cy="1060" r="22"/>
      <circle cx="455" cy="1065" r="24"/>
    </g>

    <g class="discount-badge">
      <path d="M132 372 Q360 318 600 328 Q660 520 630 710 Q400 740 150 730 Q115 560 132 372 Z"
            fill="none" stroke="#ffffff" stroke-width="9" stroke-linejoin="round"/>
      <path d="M155 420 Q385 362 612 360 Q640 540 615 706 Q400 728 172 728 Q140 580 155 420 Z"
            fill="url(#badge-burst)"/>
      <line x1="185" y1="785" x2="606" y2="772" stroke="#ffffff" stroke-width="10" stroke-linecap="round"/>
    </g>

    <g class="accent-dots" fill="#f6c514" opacity="0.75">
      <circle cx="110" cy="443" r="42"/>
      <circle cx="521" cy="701" r="40"/>
      <circle cx="418" cy="745" r="20"/>
    </g>

    <g class="info-banner">
      <polygon points="168,838 778,874 730,1037 137,1087" fill="none" stroke="#ffffff" stroke-width="4"/>
      <polygon points="98,876 764,839 730,1075 120,1068" fill="url(#info-band)"/>
      <polygon points="120,1012 742,1012 736,1054 122,1054" fill="url(#gold-band)"/>
    </g>
  </svg>

  <div class="inner-frame"></div>

  <div class="brand"><span class="brand-dot"></span>KESTAL</div>

  <h1 class="headline headline-warehouse">WAREHOUSE</h1>
  <h1 class="headline headline-sale">SALE</h1>

  <div class="player-faint player-faint-top" role="img" aria-label="Faint badminton player figure"></div>
  <div class="player-faint player-faint-left" role="img" aria-label="Faint badminton player figure"></div>
  <div class="player-main" role="img" aria-label="Silhouette of a badminton player leaping to smash with a racket"></div>

  <div class="discount discount-upto">UP TO</div>
  <div class="discount discount-number">70</div>
  <div class="discount discount-percent">%</div>
  <div class="discount discount-off">OFF</div>

  <p class="gift-note">FREE MYSTERY GIFT WHEN YOU SPEND OVER $50</p>

  <p class="event-info event-dates">5-7 Oct (10am-10pm)</p>
  <p class="event-info event-duration">3 DAYS ONLY</p>
  <p class="event-info event-location">LOCATION: Unit 5 Marlowe Fenwick Lane, Tarrowby, 2087, NSW</p>
  <p class="event-info event-frequency">EVENT WILL ONLY HAPPEN EVERY 2 YEARS.</p>

  <ul class="product-list">
    <li>RACKETS</li>
    <li>TOURNAMENT BAG</li>
    <li>APPARELS</li>
    <li>ACCESSORIES</li>
  </ul>
</div>
</body>
</html>
```